Business Card Design

we need a bussiness card for the transport company called Harvel Transport
name of contact person that should display on card is Mankirat Sekhon contact no 0478162093
we do the dry goods and frozen deliveries in melbourne every day
happy to beat any quote

Business

Contact Information for Business Card

Harvel transport
Mankirat sekhon
mob 0478162093
contact us for any refrigerator or dry goods delivery
deliver all over melbourne

```html
<!DOCTYPE html>
<html lang="en">
<head>
<meta charset="utf-8">
<title>Harvel Transport – Business Card</title>
<link rel="stylesheet" href="https://fonts.googleapis.com/css2?family=Arimo:wght@400&family=Saira+Semi+Expanded:wght@500;600;700&display=swap">
<style>
  :root {
    --backdrop: #992521;
    --card: #cbcaca;
    --brand-red: #a8291f;
    --ink: #111111;
  }
  * { margin: 0; padding: 0; box-sizing: border-box; }
  html, body { width: 1200px; height: 1000px; overflow: hidden; }
  body { background: var(--backdrop); position: relative; }

  .card { position: absolute; background: var(--card); }

  /* Portrait front card */
  .card-front { left: 82px; top: 194px; width: 378px; height: 612px; }
  .brand-mark {
    position: absolute; left: 104px; top: 40px;
    width: 170px; height: 170px; border-radius: 50%;
    background: var(--brand-red);
  }
  .front-brand {
    position: absolute; left: 0; top: 238px; width: 100%;
    text-align: center;
    font-family: "Arimo", Arial, sans-serif; font-weight: 400;
    color: var(--brand-red); font-size: 50px; line-height: 62px;
  }
  .front-name {
    position: absolute; left: 0; top: 398px; width: 100%;
    text-align: center;
    font-family: "Saira Semi Expanded", sans-serif; font-weight: 700;
    font-size: 46px; line-height: 66px; color: var(--ink);
  }
  .front-name .initial-red { color: var(--brand-red); }
  .front-name .rest-red { color: var(--brand-red); }
  .front-phone {
    position: absolute; left: 0; top: 548px; width: 100%;
    text-align: center;
    font-family: "Saira Semi Expanded", sans-serif; font-weight: 700;
    font-size: 31px; letter-spacing: 1px; color: var(--brand-red);
  }

  /* Landscape back card */
  .card-back { left: 542px; top: 311px; width: 612px; height: 378px; }
  .back-brand {
    position: absolute; left: 170px; top: 48px;
    display: flex; align-items: center; gap: 18px;
  }
  .back-brand .brand-square {
    width: 82px; height: 82px; background: var(--brand-red);
  }
  .back-brand .brand-name {
    font-family: "Arimo", Arial, sans-serif; font-weight: 400;
    color: var(--brand-red); font-size: 26px; line-height: 34px;
  }
  .back-contact, .back-coverage, .back-services {
    position: absolute; left: 0; width: 100%; text-align: center;
    font-family: "Saira Semi Expanded", sans-serif; color: var(--ink);
  }
  .back-contact { top: 176px; font-size: 21px; font-weight: 600; word-spacing: 3px; }
  .back-contact .gap { display: inline-block; width: 20px; }
  .back-coverage { top: 220px; font-size: 24px; font-weight: 700; letter-spacing: 0.5px; }
  .back-services { top: 294px; font-size: 15px; font-weight: 600; }
</style>
</head>
<body>
  <section class="card card-front" aria-label="Front of business card">
    <div class="brand-mark" aria-hidden="true"></div>
    <div class="front-brand">HARVEL<br>TRANSPORT</div>
    <div class="front-name">
      <div>M<span class="rest-red">ankirat</span></div>
      <div><span class="initial-red">S</span>ekhon</div>
    </div>
    <div class="front-phone">0478162093</div>
  </section>

  <section class="card card-back" aria-label="Back of business card">
    <div class="back-brand">
      <div class="brand-square" aria-hidden="true"></div>
      <div class="brand-name">HARVEL<br>TRANSPORT</div>
    </div>
    <p class="back-contact">Mankirat Sekhon<span class="gap"></span>mob 0478162093</p>
    <p class="back-coverage">DELIVER ALL OVER MELBOURNE</p>
    <p class="back-services">Contact us for any refrigerator or dry goods delivery</p>
  </section>
</body>
</html>
```